Mosque App design fresh look and feel

Need to create a mosque app which has half a couple of dozen pages, a login page will take you into the main information with about 6 categories, such as school, memberships, information, prayer times etc... we have 3 types of users... 1. User .. admin user 3. imam user

I have xd files available.
https://mocks.plarvio.com/view/e4f7a2d1-8b3c-4f6e-a9d2-71b5c3e8f046-2ac7/

Target Market(s)

Muslims

Font styles to use
Sans Serif

Requirements
Must have
• Great UI
Simple flow

```html
<!DOCTYPE html>
<html lang="en">
<head>
<meta charset="utf-8">
<title>Mosque App – Membership Screens</title>
<link rel="stylesheet" href="https://fonts.googleapis.com/css2?family=Montserrat:wght@400;500;600&display=swap">
<style>
  :root {
    --canvas: #d3d3d3;
    --screen: #f2f2f2;
    --green-light: #43ae85;
    --green-mid: #2e8a68;
    --green-dark: #24735a;
    --green-soft: #3f9a75;
    --grad-start: #3bb58c;
    --grad-end: #0c9e58;
    --text-grey: #6f6f6f;
    --border-grey: #cfcfcf;
    --ink: #222;
    --white: #fff;
  }
  * { box-sizing: border-box; margin: 0; padding: 0; }
  html, body { width: 1200px; height: 913px; overflow: hidden; }
  body {
    background: var(--canvas);
    font-family: "Montserrat", sans-serif;
    position: relative;
  }
  .screen {
    position: absolute;
    top: 38px;
    width: 460px;
    height: 837px;
    background: var(--screen);
    box-shadow: 0 10px 30px rgba(0,0,0,.15);
  }
  .screen--standard { left: 100px; }
  .screen--vip { left: 640px; }

  .app-header {
    position: absolute; left: 0; top: 0; width: 100%;
    background: linear-gradient(90deg, var(--grad-start), var(--grad-end));
    color: var(--white);
    display: flex; align-items: center; justify-content: center;
    font-size: 21px; font-weight: 500;
  }
  .app-header .back {
    position: absolute; left: 30px; top: 50%; transform: translateY(-50%);
    width: 14px; height: 18px;
  }

  .info-slider { position: absolute; left: 0; width: 100%; }
  .info-slider .text-box {
    position: absolute; left: 35px; width: 391px; top: 0; height: 100%;
    border: 1px solid var(--border-grey);
    padding: 0 10px;
    display: flex; align-items: center;
    font-size: 9px; line-height: 14px; color: var(--text-grey);
    letter-spacing: -0.3px;
  }
  .info-slider .arrow {
    position: absolute; top: 50%; transform: translateY(-50%);
    width: 8px; height: 14px;
  }
  .info-slider .arrow--prev { left: 17px; }
  .info-slider .arrow--next { left: 435px; }

  .tile-grid { position: absolute; left: 0; width: 100%; display: grid; }
  .tile {
    color: var(--white);
    display: flex; flex-direction: column; align-items: center; justify-content: center;
    font-size: 13.5px; font-weight: 500; text-align: center; line-height: 13px;
  }
  .tile svg { width: 54px; height: 46px; margin-bottom: 10px; }
  .tile--light { background: var(--green-light); }
  .tile--mid { background: var(--green-mid); }
  .tile--dark { background: var(--green-dark); }
  .tile--soft { background: var(--green-soft); }

  .prayer-panel {
    position: absolute; left: 0; width: 100%;
    background: var(--green-dark);
  }
  .prayer-table {
    position: absolute; left: 35px; width: 390px;
    background: var(--white);
  }
  .prayer-tabs { display: grid; grid-template-columns: 1fr 1fr; height: 48px; }
  .prayer-tabs span {
    display: flex; align-items: center; justify-content: center;
    color: var(--white); font-size: 16px; font-weight: 500;
  }
  .prayer-tabs .tab--active { background: var(--green-light); }
  .prayer-tabs .tab { background: var(--green-dark); border: 1px solid var(--green-light); border-left: 0; border-bottom: 0; }
  .prayer-date {
    height: 38px; display: flex; align-items: center; justify-content: center;
    font-size: 13px; font-weight: 500; color: var(--ink);
    border-bottom: 1px solid #ddd;
  }
  .prayer-row { display: grid; grid-template-columns: repeat(6, 1fr); height: 48px; }
  .prayer-row div {
    border-right: 1px solid #ddd;
    display: flex; flex-direction: column; align-items: center; justify-content: center;
    font-size: 11px; color: var(--ink); line-height: 18px;
  }
  .prayer-row div:last-child { border-right: 0; }
  .prayer-row .time { color: #555; }

  .upgrade-button {
    position: absolute; left: 35px; top: 745px; width: 390px; height: 53px;
    background: linear-gradient(90deg, var(--grad-start), var(--grad-end));
    color: var(--white); font-size: 17px; font-weight: 500;
    display: flex; align-items: center; justify-content: center;
  }
</style>
</head>
<body>

<svg width="0" height="0" style="position:absolute">
  <defs>
    <symbol id="icon-mosque" viewBox="0 0 54 46">
      <g fill="#fff">
        <path d="M27 2 l1 3 -2 0z"/>
        <path d="M18 24 C18 14 27 9 27 9 C27 9 36 14 36 24z"/>
        <rect x="17" y="24" width="20" height="22"/>
        <rect x="4" y="14" width="5" height="32"/>
        <rect x="45" y="14" width="5" height="32"/>
        <path d="M3 14 l3.5 -6 3.5 6z M44 14 l3.5 -6 3.5 6z"/>
        <rect x="9" y="28" width="8" height="18"/>
        <rect x="37" y="28" width="8" height="18"/>
      </g>
      <g fill="#43ae85">
        <path d="M23 46 v-8 a4 4 0 0 1 8 0 v8z"/>
        <rect x="11" y="33" width="3" height="6" rx="1.5"/>
        <rect x="40" y="33" width="3" height="6" rx="1.5"/>
      </g>
    </symbol>
    <symbol id="icon-donation" viewBox="0 0 54 46">
      <circle cx="27" cy="9" r="8" fill="#fff"/>
      <text x="27" y="13" font-size="11" font-weight="600" text-anchor="middle" fill="#2e8a68" font-family="Montserrat, sans-serif">$</text>
      <rect x="8" y="20" width="38" height="4" fill="#fff"/>
      <rect x="11" y="26" width="32" height="20" fill="#fff"/>
      <rect x="16" y="31" width="22" height="7" fill="none" stroke="#2e8a68" stroke-width="2"/>
    </symbol>
    <symbol id="icon-suggestion" viewBox="0 0 54 46">
      <path d="M20 8 l5 -4 3 4 4 -5 3 5z" fill="#fff"/>
      <rect x="8" y="12" width="38" height="5" fill="#fff"/>
      <rect x="11" y="19" width="32" height="24" fill="#fff"/>
      <ellipse cx="27" cy="30" rx="8" ry="4" fill="none" stroke="#24735a" stroke-width="2"/>
    </symbol>
    <symbol id="icon-people" viewBox="0 0 54 46">
      <g fill="#fff">
        <circle cx="13" cy="10" r="6"/><circle cx="41" cy="10" r="6"/>
        <circle cx="27" cy="16" r="8"/>
        <path d="M2 30 a11 10 0 0 1 22 0z M30 30 a11 10 0 0 1 22 0z"/>
        <path d="M11 44 a16 15 0 0 1 32 0z"/>
      </g>
    </symbol>
    <symbol id="icon-invite" viewBox="0 0 54 46">
      <g fill="#fff">
        <path d="M6 20 L27 36 L48 20 V46 H6z"/>
        <rect x="14" y="2" width="26" height="26"/>
      </g>
      <path d="M27 7 l2.4 5 5.4 .6 -4 3.7 1.1 5.3 -4.9 -2.7 -4.9 2.7 1.1 -5.3 -4 -3.7 5.4 -.6z" fill="#3f9a75"/>
      <path d="M6 46 L22 32 M48 46 L32 32" stroke="#3f9a75" stroke-width="2"/>
    </symbol>
    <symbol id="chev-left" viewBox="0 0 8 14"><path d="M7 1 L1 7 L7 13" fill="none" stroke="#999" stroke-width="1.3"/></symbol>
    <symbol id="chev-right" viewBox="0 0 8 14"><path d="M1 1 L7 7 L1 13" fill="none" stroke="#999" stroke-width="1.3"/></symbol>
    <symbol id="back-white" viewBox="0 0 14 18"><path d="M11 2 L4 9 L11 16" fill="none" stroke="#fff" stroke-width="2.2"/></symbol>
  </defs>
</svg>

<!-- Standard membership screen -->
<section class="screen screen--standard">
  <header class="app-header" style="height:68px">
    <svg class="back"><use href="#back-white"/></svg>
    Standard Membership
  </header>

  <div class="info-slider" style="top:101px;height:103px">
    <svg class="arrow arrow--prev"><use href="#chev-left"/></svg>
    <p class="text-box">Lorem Ipsum is simply dummy text of the printing and typesetting industry. Lorem Ipsum has been the industry's standard dummy text ever since the 1500s, when an unknown printer took a galley of type and scrambled it to make a type specimen book. It has survived not only five centuries, but also the leap into electronic typesetting, remaining essentially unchanged.</p>
    <svg class="arrow arrow--next"><use href="#chev-right"/></svg>
  </div>

  <nav class="tile-grid" style="top:229px;height:150px;grid-template-columns:152px 154px 154px">
    <div class="tile tile--light"><svg><use href="#icon-mosque"/></svg>My Madrassa</div>
    <div class="tile tile--mid"><svg><use href="#icon-donation"/></svg>My Donation</div>
    <div class="tile tile--dark"><svg><use href="#icon-suggestion"/></svg>Suggestion Box</div>
  </nav>

  <div class="info-slider" style="top:406px;height:103px">
    <svg class="arrow arrow--prev"><use href="#chev-left"/></svg>
    <p class="text-box">Lorem Ipsum is simply dummy text of the printing and typesetting industry. Lorem Ipsum has been the industry's standard dummy text ever since the 1500s, when an unknown printer took a galley of type and scrambled it to make a type specimen book. It has survived not only five centuries, but also the leap into electronic typesetting, remaining essentially unchanged.</p>
    <svg class="arrow arrow--next"><use href="#chev-right"/></svg>
  </div>

  <section class="prayer-panel" style="top:535px;height:191px">
    <div class="prayer-table" style="top:29px">
      <div class="prayer-tabs"><span class="tab--active">Jamat Times</span><span class="tab">Prayers Start Times</span></div>
      <div class="prayer-date">Friday January 22, 2021</div>
      <div class="prayer-row">
        <div>Prayers<span class="time">Timing</span></div>
        <div>Fajr<span class="time">04:00</span></div>
        <div>Duhr<span class="time">01:30</span></div>
        <div>Asar<span class="time">04:30</span></div>
        <div>Magrib<span class="time">05:45</span></div>
        <div>Isha<span class="time">08:45</span></div>
      </div>
    </div>
  </section>

  <div class="upgrade-button">Upgrade Membership</div>
</section>

<!-- VIP membership screen -->
<section class="screen screen--vip">
  <header class="app-header" style="height:62px">
    <svg class="back"><use href="#back-white"/></svg>
    VIP Membership
  </header>

  <div class="info-slider" style="top:94px;height:96px">
    <svg class="arrow arrow--prev"><use href="#chev-left"/></svg>
    <p class="text-box">Lorem Ipsum is simply dummy text of the printing and typesetting industry. Lorem Ipsum has been the industry's standard dummy text ever since the 1500s, when an unknown printer took a galley of type and scrambled it to make a type specimen book. It has survived not only five centuries, but also the leap into electronic typesetting, remaining essentially unchanged.</p>
    <svg class="arrow arrow--next"><use href="#chev-right"/></svg>
  </div>

  <nav class="tile-grid" style="top:220px;height:140px;grid-template-columns:152px 154px 154px">
    <div class="tile tile--light"><svg><use href="#icon-mosque"/></svg>My Madrassa</div>
    <div class="tile tile--mid"><svg><use href="#icon-donation"/></svg>My Donation</div>
    <div class="tile tile--dark"><svg><use href="#icon-suggestion"/></svg>Suggestion Box</div>
  </nav>
  <nav class="tile-grid" style="top:360px;height:140px;grid-template-columns:230px 230px">
    <div class="tile tile--dark"><svg><use href="#icon-people"/></svg>DPCA<br>Committee Members</div>
    <div class="tile tile--soft"><svg><use href="#icon-invite"/></svg>My Invites (2)</div>
  </nav>

  <div class="info-slider" style="top:525px;height:96px">
    <svg class="arrow arrow--prev"><use href="#chev-left"/></svg>
    <p class="text-box">Lorem Ipsum is simply dummy text of the printing and typesetting industry. Lorem Ipsum has been the industry's standard dummy text ever since the 1500s, when an unknown printer took a galley of type and scrambled it to make a type specimen book. It has survived not only five centuries, but also the leap into electronic typesetting, remaining essentially unchanged.</p>
    <svg class="arrow arrow--next"><use href="#chev-right"/></svg>
  </div>

  <section class="prayer-panel" style="top:641px;height:176px">
    <div class="prayer-table" style="top:27px">
      <div class="prayer-tabs" style="height:46px"><span class="tab--active">Jamat Times</span><span class="tab">Prayers Start Times</span></div>
      <div class="prayer-date" style="height:34px">Friday January 22, 2021</div>
      <div class="prayer-row" style="height:46px">
        <div>Prayers<span class="time">Timing</span></div>
        <div>Fajr<span class="time">04:00</span></div>
        <div>Duhr<span class="time">01:30</span></div>
        <div>Asar<span class="time">04:30</span></div>
        <div>Magrib<span class="time">05:45</span></div>
        <div>Isha<span class="time">08:45</span></div>
      </div>
    </div>
  </section>
</section>

</body>
</html>
```